tidal box

TIDAL BOX mobile technology servicesPhone and tablet repairs, screens data recovery.

Industry/Entity Type

Data Recovery

Contact Information for Business Card

0491 573 086

Colors
33a6d7
f04a50
0a90cc
e34197

Requirements
Must have
• Liam hardy
Nice to have
• White background

```html
<!DOCTYPE html>
<html lang="en">
<head>
<meta charset="utf-8">
<title>tidal box – business card</title>
<link rel="stylesheet" href="https://fonts.googleapis.com/css2?family=Montserrat:wght@600;700;800&display=swap">
<style>
  :root {
    --blue: #33a6d7;
    --blue-deep: #0a90cc;
    --red: #f04a50;
    --card: #f3f4f4;
    --page: #ffffff;
  }
  * { margin: 0; padding: 0; box-sizing: border-box; }
  html, body {
    width: 1200px; height: 742px; overflow: hidden;
    background: var(--page);
  }
  .card {
    position: absolute; left: 20px; top: 20px;
    width: 1160px; height: 702px;
    background: var(--card);
    font-family: "Montserrat", Arial, sans-serif;
  }
  .phone-label {
    position: absolute; left: 102px; top: 72px;
    font-size: 34px; font-weight: 600; letter-spacing: 1px;
    color: var(--blue);
  }
  .phone-number {
    position: absolute; left: 54px; top: 114px;
    font-size: 42px; font-weight: 700; letter-spacing: 2px;
    color: var(--red);
  }
  .person {
    position: absolute; left: 800px; top: 56px; width: 320px;
    text-align: center; font-variant: small-caps;
  }
  .person-first {
    font-size: 64px; font-weight: 600; line-height: 1;
    color: var(--blue);
  }
  .person-last {
    margin-top: 6px;
    font-size: 40px; font-weight: 700; line-height: 1;
    color: var(--red);
  }
  .device-art {
    position: absolute; left: 424px; top: 184px;
    width: 308px; height: 160px; border-radius: 26px;
    background: linear-gradient(180deg, #5ab7de 0%, var(--blue) 100%);
  }
  .brand-name {
    position: absolute; left: 0; top: 340px; width: 1160px;
    text-align: center;
    font-size: 132px; font-weight: 800; letter-spacing: 4px; line-height: 1.1;
    color: var(--red);
  }
  .tagline {
    position: absolute; left: 86px; top: 522px; width: 1020px;
    font-size: 33px; font-weight: 600; line-height: 65px;
    font-variant: small-caps; letter-spacing: 1.5px;
    color: var(--blue);
  }
</style>
</head>
<body>
  <div class="card">
    <div class="phone-label">PHONE NO:</div>
    <div class="phone-number">0491 573 086</div>

    <div class="person">
      <div class="person-first">Liam</div>
      <div class="person-last">hardy</div>
    </div>

    <div class="device-art" role="img" aria-label="Illustration of a smartphone with a cracked screen"></div>

    <div class="brand-name">tidal box</div>

    <p class="tagline">mobile technology services Phone And<br>tablet repairs, screens data recovery.</p>
  </div>
</body>
</html>
```